Arabic Alphabet Art Contest

Arabic Studies at Brookhaven

Arabic Art Contest

Express yourselves through Arabic Art

Calling all student artists to participate in Brookhaven's 1st Arabic Art Contest

The Arabic Alphabet is made up of 28 letters. Let's see you artistic skills by creating a poster with all of the Arabic Alphabets

Art Submissions due by: February 1st, 2021
Submit all entries to Mr. Qudsi

Grade Prize: $100 Vendrix Gift Card
Second Prize: $75 Vendrix Gift Card
3rd Prize: $50 Vendrix Gift Card
4th Prize: $25 Gift Card

```html
<!DOCTYPE html>
<html lang="en">
<head>
<meta charset="utf-8">
<title>Arabic Art Contest – Brookhaven</title>
<link rel="stylesheet" href="https://fonts.googleapis.com/css2?family=Audiowide&family=Marck+Script&family=Questrial&display=swap">
<style>
  :root {
    --paper: #ffffff;
    --navy: #1b1f5c;
    --script-blue: #1f5a8f;
    --teal: #2b8ca3;
    --orange: #f39a1c;
    --ink: #111111;
    --body: #222222;
    --ornament: #4aa3c6;
  }
  html, body { margin: 0; padding: 0; overflow: hidden; background: var(--paper); }
  .poster {
    position: relative;
    width: 849px;
    height: 1200px;
    overflow: hidden;
    background: var(--paper);
    font-family: "Questrial", sans-serif;
  }
  .letter-backdrop {
    position: absolute;
    left: 0; top: 240px;
    width: 849px; height: 700px;
    background:
      radial-gradient(ellipse 220px 260px at 140px 260px, rgba(230,120,120,0.14), transparent 70%),
      radial-gradient(ellipse 260px 240px at 420px 330px, rgba(120,140,190,0.16), transparent 70%),
      radial-gradient(ellipse 220px 260px at 700px 280px, rgba(120,190,140,0.14), transparent 70%),
      radial-gradient(ellipse 300px 200px at 420px 580px, rgba(150,150,170,0.12), transparent 70%);
  }
  .basmala {
    position: absolute;
    top: 90px;
    width: 196px; height: 26px;
    background: linear-gradient(90deg, #1a1a1a, #333333);
    border-radius: 2px;
  }
  .basmala--left { left: 78px; }
  .basmala--right { left: 582px; }
  .school-name {
    position: absolute;
    top: 82px; left: 0; width: 849px;
    display: flex; justify-content: center; align-items: center; gap: 10px;
    font-family: "Audiowide", sans-serif;
    font-size: 24px;
    color: var(--navy);
  }
  .school-name__dot {
    width: 14px; height: 14px; border-radius: 50%;
    background: var(--navy);
  }
  .title {
    position: absolute;
    top: 222px; left: 0; width: 849px;
    margin: 0;
    text-align: center;
    font-family: "Audiowide", sans-serif;
    font-weight: 400;
    font-size: 56px;
    letter-spacing: 2px;
    color: var(--navy);
    text-transform: uppercase;
  }
  .tagline {
    position: absolute;
    top: 318px; left: 0; width: 849px;
    margin: 0;
    text-align: center;
    font-family: "Marck Script", cursive;
    font-size: 38px;
    color: var(--script-blue);
  }
  .intro {
    position: absolute;
    left: 68px; width: 720px;
    margin: 0;
    font-size: 29px;
    line-height: 33px;
    color: var(--body);
  }
  .intro--call { top: 404px; }
  .intro--alphabet { top: 512px; }
  .deadline {
    position: absolute;
    left: 68px; top: 648px;
    margin: 0;
    font-family: "Audiowide", sans-serif;
    font-size: 21px;
    line-height: 30px;
    color: var(--teal);
    text-transform: uppercase;
  }
  .place, .prize {
    position: absolute;
    width: 160px;
    margin-left: -80px;
    text-align: center;
  }
  .place {
    font-family: "Questrial", sans-serif;
    color: var(--ink);
  }
  .prize {
    font-family: "Audiowide", sans-serif;
    color: var(--orange);
  }
  .place--1 { left: 424px; top: 790px; font-size: 58px; }
  .prize--1 { left: 428px; top: 848px; font-size: 40px; }
  .place--2 { left: 600px; top: 860px; font-size: 36px; }
  .prize--2 { left: 600px; top: 904px; font-size: 32px; }
  .place--3 { left: 245px; top: 860px; font-size: 36px; }
  .prize--3 { left: 243px; top: 904px; font-size: 32px; }
  .place--4 { left: 421px; top: 920px; font-size: 30px; }
  .prize--4 { left: 421px; top: 953px; font-size: 30px; }
  .gift-card {
    position: absolute;
    top: 1020px; left: 0; width: 849px;
    margin: 0;
    text-align: center;
    font-family: "Audiowide", sans-serif;
    font-size: 27px;
    letter-spacing: 1px;
    color: var(--orange);
    text-transform: uppercase;
  }
  .flourish {
    position: absolute;
    left: 346px; top: 1102px;
    width: 158px; height: 70px;
    background: radial-gradient(ellipse at center, rgba(74,163,198,0.55), rgba(74,163,198,0.12) 70%, transparent 75%);
  }
</style>
</head>
<body>
<main class="poster">
  <div class="letter-backdrop" role="img" aria-label="Faint scattered Arabic letters in red, blue and green"></div>

  <div class="basmala basmala--left" role="img" aria-label="Square Kufic calligraphy of the Basmala"></div>
  <div class="school-name"><span class="school-name__dot"></span>Brookhaven</div>
  <div class="basmala basmala--right" role="img" aria-label="Square Kufic calligraphy of the Basmala"></div>

  <h1 class="title">Arabic Art Contest</h1>
  <p class="tagline">express yourselves through arabic art</p>

  <p class="intro intro--call">Calling all student artists to participate in Brookhaven's 1st Arabic Art Contest</p>
  <p class="intro intro--alphabet">The Arabic Alphabet is made up of 28 letters. Let's see you artistic skills by creating a poster with all of the Arabic Alphabets</p>

  <p class="deadline">Art submissions due by: February 1st, 2021<br>Submit all entries to Mr. Qudsi</p>

  <div class="place place--1">1</div>
  <div class="prize prize--1">$100</div>
  <div class="place place--3">3</div>
  <div class="prize prize--3">$50</div>
  <div class="place place--2">2</div>
  <div class="prize prize--2">$75</div>
  <div class="place place--4">4</div>
  <div class="prize prize--4">$20</div>

  <p class="gift-card">Vendrix Gift Card</p>

  <div class="flourish" role="img" aria-label="Blue scrolled ornamental flourish"></div>
</main>
</body>
</html>
```